Webdesign für Management Coaching
Zielgruppe
Ich bin Coach/biete Coaching-Leistungen an.
Zielgruppe: Fokus auf Führungskräfte/Entscheider/Management mit technischem Hintergrund (Forschung & Entwicklung, Engineering, Technik, Maschinenbau, Naturwissenschaften)
Coaching-Schwerpunkte: Sinn-Coaching, Begleitung bei Umbrüchen und Veränderungen (privat & beruflich), Sparring & Reflexion
Aufgabenstellung
Gewünscht wurde ein helles Design, das die Logo-Farben aufnimmt. Ausrichtung am Logo & den verwendeten Farben, Schriften
Bilder: Ich werde noch Fotos beim Fotografen machen, die eingebunden werden sollen (Profil, etc.). Bitte Anhaltspunkte nennen, worauf ich die Fotografin hinweisen soll/welche Motive ins Konzept passen.

```html
<!DOCTYPE html>
<html lang="de">
<head>
<meta charset="utf-8">
<title>Lehrbach Coaching &amp; Beratung</title>
<link href="https://fonts.googleapis.com/css2?family=EB+Garamond:wght@400;500;600;700&family=Mrs+Saint+Delafield&display=swap" rel="stylesheet">
<style>
:root{
  --blue:#7a9db5;
  --teal:#7a9eab;
  --grey-btn:#a8b2ba;
  --ink:#2e2e2e;
  --hero-top:#f7f8f9;
  --hero-bottom:#e6eeee;
  --white:#ffffff;
  --icon-tint:#dfe8ee;
  --marker:#ff0000;
}
*{margin:0;padding:0;box-sizing:border-box}
html,body{width:1200px;height:2292px;overflow:hidden}
body{position:relative;font-family:"EB Garamond",Georgia,serif;color:var(--ink);background:var(--white)}
.abs{position:absolute}
.script{font-family:"Mrs Saint Delafield",cursive;font-weight:400}
.marker{position:absolute;left:34px;width:34px;height:34px;border-radius:50%;background:var(--marker)}

.hero{position:absolute;left:0;top:0;width:1200px;height:765px;
  background:linear-gradient(170deg,var(--hero-top) 0%,var(--hero-top) 45%,var(--hero-bottom) 100%)}
.nav{position:absolute;left:100px;top:104px;display:flex;gap:20px;font-size:30px;color:var(--blue)}
.brand{position:absolute;left:529px;top:58px;width:142px;height:142px;border-radius:50%;
  border:1px solid var(--blue);display:flex;align-items:center;justify-content:center;text-align:center;
  font-size:17px;line-height:1.2;color:var(--blue);letter-spacing:.05em}
.social{position:absolute;top:110px;width:30px;height:30px;border-radius:50%;background:var(--blue)}
.btn{position:absolute;display:flex;align-items:center;justify-content:center;color:var(--white);
  font-weight:600;font-size:16px;border-radius:4px;background:var(--blue)}
.btn.grey{background:var(--grey-btn)}
.hero-kicker{left:100px;top:234px;font-size:38px;color:var(--blue)}
.hero-title{left:100px;top:290px;font-size:84px;line-height:90px;color:var(--blue)}
.hero-text{left:100px;top:489px;width:560px;font-size:15.8px;line-height:23.3px}
.hero-photo{left:756px;top:293px;width:347px;height:472px;border-radius:160px 160px 0 0;
  background:linear-gradient(180deg,#c9a68a 0%,#d8c0ae 30%,#b9d0e6 55%,#a9c4df 100%)}

.profile-photo{left:140px;top:964px;width:334px;height:334px;border-radius:50%;
  background:radial-gradient(circle at 50% 45%,#d6b59c 0%,#c8d8e6 45%,#b8ccdc 75%,#dcd8d0 100%)}
.eyebrow{font-size:14px;letter-spacing:.28em;font-weight:600;text-transform:uppercase}
.about-eyebrow{left:535px;top:876px;color:#555b60}
.about-title{left:535px;top:906px;font-size:40px;line-height:46px;font-weight:700;color:var(--blue)}
.about-text{left:535px;top:1016px;width:525px;font-size:16.2px;line-height:23.3px}
.about-text p+p{margin-top:23.3px}

.services{position:absolute;left:0;top:1479px;width:1200px;height:813px;background:var(--teal);color:var(--white)}
.svc-eyebrow{left:0;top:95px;width:1200px;text-align:center}
.svc-title{left:0;top:105px;width:1200px;text-align:center;font-size:82px}
.svc-card{position:absolute;top:234px;width:320px;text-align:center}
.svc-icon{width:180px;height:180px;margin:0 auto;border-radius:50%;background:var(--white);
  display:flex;align-items:center;justify-content:center}
.svc-icon-fill{width:84px;height:84px;border-radius:50%;background:var(--icon-tint)}
.svc-name{height:58px;margin-top:8px;display:flex;align-items:flex-end;justify-content:center;font-size:26px;font-weight:700}
.svc-name.script{font-size:44px;font-weight:400}
.svc-text{margin-top:10px;font-size:16.2px;line-height:23.3px;font-weight:500}
</style>
</head>
<body>

<section class="hero">
  <nav class="nav script"><span>Home</span><span>Leistungen</span><span>Profil</span><span>Blog</span></nav>
  <div class="brand">Lehrbach<br>Coaching</div>
  <span class="social" style="left:803px" aria-label="Messenger"></span>
  <span class="social" style="left:861px" aria-label="Soziales Netzwerk"></span>
  <span class="social" style="left:920px" aria-label="Berufsnetzwerk"></span>
  <a class="btn" style="left:982px;top:101px;width:117px;height:43px">Kontakt</a>

  <div class="abs script hero-kicker">Für technische Visionäre</div>
  <h1 class="abs script hero-title">Coaching, das Sie<br>zum Erfolg führt</h1>
  <p class="abs hero-text">Beratung für Führungskräfte und Entscheider mit technischem Hintergrund.<br>Mit einer fundierten Expertise in den Bereichen Forschung &amp; Entwicklung, Engineering, Technik, Maschinenbau und Naturwissenschaften stehe ich Ihnen zur Seite, um Ihre beruflichen und persönlichen Herausforderungen zu meistern.</p>
  <a class="btn" style="left:100px;top:607px;width:171px;height:43px">Mehr über mich</a>
  <a class="btn grey" style="left:288px;top:607px;width:198px;height:43px">Termin vereinbaren</a>
  <div class="abs hero-photo" role="img" aria-label="Porträt des Coaches mit verschränkten Armen im hellblauen Hemd"></div>
</section>

<section>
  <div class="abs profile-photo" role="img" aria-label="Profilfoto des Coaches, nachdenklich, in hellem Büro"></div>
  <div class="abs eyebrow about-eyebrow">Matthias Lehrbach</div>
  <h2 class="abs about-title">Profitieren Sie von<br>meiner Expertise</h2>
  <div class="abs about-text">
    <p>Ich bin Matthias Lehrbach, zertifizierter Coach mit einer Leidenschaft für die Entwicklung von Führungskräften und Entscheidern im technischen Bereich. Mit einem Hintergrund in [Fachgebiet] und einer langjährigen Erfahrung in der Unterstützung von Menschen auf ihrem Weg zu persönlichem und beruflichem Wachstum, stehe ich Ihnen als vertrauensvoller Begleiter zur Seite.</p>
    <p>Mein Coaching-Ansatz vereint technische Expertise mit einem tiefen Verständnis für persönliche Entwicklung und Sinnhaftigkeit in der Führung. In unserer Zusammenarbeit schaffen wir einen Raum für Reflexion, Sparring und zielgerichtete Veränderung. Meine Mission ist es, Sie dabei zu unterstützen, nicht nur beruflichen Erfolg zu erzielen, sondern auch eine erfüllende und sinnvolle Führungskraft zu werden.</p>
  </div>
  <a class="btn" style="left:535px;top:1322px;width:327px;height:42px">Erfahren Sie mehr über mein Angebot</a>
</section>

<section class="services">
  <div class="abs eyebrow svc-eyebrow">Leistungen</div>
  <h2 class="abs script svc-title">Gemeinsam auf Kurs gehen</h2>

  <div class="svc-card" style="left:101px;top:231px">
    <div class="svc-icon"><div class="svc-icon-fill" role="img" aria-label="Symbol für Coaching im Dialog"></div></div>
    <div class="svc-name script">Coaching</div>
    <p class="svc-text">In meinem Coaching legen wir gemeinsam den Fokus auf bedeutungsvolle Veränderungen in Ihrem Leben und Ihrer beruflichen Laufbahn. Ich unterstütze Sie in den Bereichen Sinn-Coaching, begleite Sie durch Umbrüche und Veränderungen – sei es im privaten oder beruflichen Kontext – und biete Ihnen Sparring und Reflexion auf höchstem Niveau.</p>
  </div>

  <div class="svc-card" style="left:440px">
    <div class="svc-icon"><div class="svc-icon-fill" role="img" aria-label="Symbol für Wachstum und Nutzen"></div></div>
    <div class="svc-name">Ihr Nutzen</div>
    <p class="svc-text">Als erfahrener Coach verbinde ich Fachkompetenz mit Einfühlungsvermögen, um Ihnen nicht nur praktische Werkzeuge an die Hand zu geben, sondern auch einen Raum für persönliches Wachstum und Entfaltung zu schaffen. Ihr Erfolg und Ihre Zufriedenheit stehen im Mittelpunkt meiner Arbeit.</p>
  </div>

  <div class="svc-card" style="left:778px">
    <div class="svc-icon"><div class="svc-icon-fill" role="img" aria-label="Symbol für die Zielgruppe"></div></div>
    <div class="svc-name">Zielgruppe</div>
    <p class="svc-text">Meine Dienstleistungen richten sich an Führungskräfte und Entscheider in technischen Disziplinen. Ob Sie in der Forschung tätig sind, im Bereich Engineering, Technik, Maschinenbau oder Naturwissenschaften – ich bin hier, um Sie auf Ihrem Weg zu begleiten.</p>
  </div>
</section>

<span class="marker" style="top:99px"></span>
<span class="marker" style="top:233px"></span>
<span class="marker" style="top:402px"></span>
<span class="marker" style="top:1622px"></span>
<span class="marker" style="top:1929px"></span>

</body>
</html>
```